Calderwell Homes

To produce a business card design for our newly established house building and development company, We have had a logo design done please see attached, our slogan is "building your home sweet home"
Contact Information for Business Card
Adress on card needs to Read - 47 Hollowmere Lane, Kettering, Northamptonshire NN14 3QX. Director name Mark Ellery
Requirements
Must have
- Web adress is www.calderwell-homes.co.uk
- Email address is info@calderwell-homes.co.uk
- phone number 07700 900418

```html
<!DOCTYPE html>
<html lang="en">
<head>
<meta charset="utf-8">
<title>Calderwell Homes – Business Card</title>
<link rel="stylesheet" href="https://fonts.googleapis.com/css2?family=Lato:wght@400;700;900&display=swap">
<style>
  :root {
    --brand-green: #7dc12f;
    --ink-dark: #2b2b2b;
    --ink-mid: #555555;
    --rule-grey: #a9a9a9;
    --card-white: #ffffff;
    --card-black: #141414;
    --card-black-sheen: #2e2e2e;
    --backdrop: #ecebe8;
  }
  * { box-sizing: border-box; margin: 0; padding: 0; }
  html, body {
    width: 1200px; height: 1024px; overflow: hidden;
    background: var(--backdrop);
    font-family: "Lato", sans-serif;
  }
  .canvas { position: relative; width: 1200px; height: 1024px; }
  .card {
    position: absolute; left: 190px; width: 820px; height: 468px;
    box-shadow: 0 10px 28px rgba(0,0,0,0.18);
    overflow: hidden;
  }
  /* front */
  .card--front { top: 30px; background: var(--card-white); }
  .brand-block {
    position: absolute; left: 44px; top: 150px; width: 300px;
  }
  .brand-name {
    color: var(--brand-green); font-weight: 900;
    font-size: 40px; line-height: 1.02; letter-spacing: 1px;
    text-transform: uppercase;
  }
  .brand-rule { margin-top: 14px; height: 1px; background: var(--rule-grey); width: 290px; }
  .brand-slogan {
    margin-top: 8px; color: var(--brand-green);
    font-size: 11px; letter-spacing: 3.6px; text-transform: uppercase;
  }
  .front-divider {
    position: absolute; left: 390px; top: 60px; width: 1px; height: 348px;
    background: var(--rule-grey);
  }
  .contact-block { position: absolute; left: 430px; top: 66px; width: 360px; }
  .person-name {
    color: var(--brand-green); font-weight: 700; font-size: 30px;
    text-transform: uppercase; letter-spacing: 0.5px;
  }
  .person-role {
    color: var(--ink-dark); font-weight: 900; font-size: 17px;
    text-transform: uppercase; margin-top: 2px;
  }
  .address { margin-top: 40px; color: var(--ink-dark); font-size: 18px; line-height: 1.4; }
  .contact-rule { margin: 26px 0 24px; height: 1px; width: 330px; background: var(--rule-grey); }
  .contact-list { list-style: none; }
  .contact-item {
    display: flex; align-items: center; gap: 12px;
    color: var(--ink-dark); font-size: 18px; line-height: 1.75;
  }
  .contact-icon { width: 16px; height: 16px; fill: var(--brand-green); flex: none; }
  /* back */
  .card--back {
    top: 526px;
    background: linear-gradient(125deg, var(--card-black) 0%, var(--card-black-sheen) 38%, var(--card-black) 70%, #0b0b0b 100%);
  }
  .back-brand { position: absolute; right: 60px; bottom: 86px; text-align: left; width: 440px; }
  .back-brand .brand-name { font-size: 46px; }
  .back-brand .brand-rule { width: 440px; background: #8a8a8a; }
  .back-slogan {
    margin-top: 10px; color: #ffffff; font-size: 22px; letter-spacing: 0.5px;
  }
</style>
</head>
<body>
<main class="canvas">
  <section class="card card--front" aria-label="Business card front">
    <div class="brand-block">
      <p class="brand-name">Calderwell Homes</p>
      <div class="brand-rule"></div>
      <p class="brand-slogan">Building your home sweet home</p>
    </div>
    <div class="front-divider"></div>
    <div class="contact-block">
      <h1 class="person-name">Mark Ellery</h1>
      <p class="person-role">Director</p>
      <p class="address">47 Hollowmere Lane, Kettering,<br>Northamptonshire NN14 3QX.</p>
      <div class="contact-rule"></div>
      <ul class="contact-list">
        <li class="contact-item">
          <svg class="contact-icon" viewBox="0 0 24 24" aria-hidden="true"><path d="M6.6 10.8a15.1 15.1 0 0 0 6.6 6.6l2.2-2.2a1 1 0 0 1 1-.25 11.4 11.4 0 0 0 3.6.57 1 1 0 0 1 1 1V20a1 1 0 0 1-1 1A17 17 0 0 1 3 4a1 1 0 0 1 1-1h3.5a1 1 0 0 1 1 1c0 1.25.2 2.45.57 3.6a1 1 0 0 1-.25 1z"/></svg>
          07700 900418
        </li>
        <li class="contact-item">
          <svg class="contact-icon" viewBox="0 0 24 24" aria-hidden="true"><path d="M2 5h20v14H2z M4 7v.4l8 5.2 8-5.2V7z" fill-rule="evenodd"/></svg>
          info@calderwell-homes.co.uk
        </li>
        <li class="contact-item">
          <svg class="contact-icon" viewBox="0 0 24 24" aria-hidden="true"><circle cx="12" cy="12" r="10"/><path d="M2 12h20M12 2c3 3 3 17 0 20M12 2c-3 3-3 17 0 20" stroke="#fff" stroke-width="1.4" fill="none"/></svg>
          www.calderwell-homes.co.uk
        </li>
      </ul>
    </div>
  </section>

  <section class="card card--back" aria-label="Business card back">
    <div class="back-brand">
      <p class="brand-name">Calderwell Homes</p>
      <div class="brand-rule"></div>
      <p class="back-slogan">building your home sweet home</p>
    </div>
  </section>
</main>
</body>
</html>
```